TORVEL Industrial Maintenance

I offer repair and maintenance services of industrial mechanics in Quebec. I would like a creation that reflects confidence, competence, professionalism and dynamism. I like the orange color and the blue color.

Target Market(s)

Industries and Manufacturing companies using industrial machinery for the manufacture of their products.

Industry/Entity Type

Manufacturing

Contact Information for Business Card

TORVEL Maintenance Industrielle
Tél: (450)-318-5947
Courriel: torvel.mnt@boitemel-exemple.com

Font styles to use
Sans Serif

Colors
f78f20
0455a3

Requirements
Must have
• My company name: TORVEL Maintenance Industrielle My phone: (450) -318-5947 My email: torvel.mnt@boitemel-exemple.com
Nice to have
• Integrate a representative logo of the mechanics (gears, mechanical parts)

```html
<!DOCTYPE html>
<html lang="fr">
<head>
<meta charset="utf-8">
<title>TORVEL Maintenance Industrielle – Carte d'affaires</title>
<link rel="stylesheet" href="https://fonts.googleapis.com/css2?family=Montserrat:wght@400;500;600;700;800&display=swap">
<style>
  :root {
    --orange: #f0962a;
    --charcoal: #333333;
    --ink: #1f1f1f;
    --muted: #4a4a4a;
    --paper: #ffffff;
    --backdrop: #e7e9ec;
  }
  * { box-sizing: border-box; margin: 0; padding: 0; }
  html, body { width: 1200px; height: 675px; overflow: hidden; }
  body {
    background: var(--backdrop);
    font-family: "Montserrat", sans-serif;
    position: relative;
  }
  .business-card {
    position: absolute;
    left: 100px; top: 52px;
    width: 1000px; height: 572px;
    background: var(--paper);
    box-shadow: 0 6px 24px rgba(0,0,0,0.12);
    overflow: hidden;
  }
  .brand {
    position: absolute;
    left: 130px; top: 250px;
    width: 340px;
    text-align: center;
  }
  .brand-name {
    font-weight: 800;
    font-size: 64px;
    letter-spacing: 4px;
    color: var(--orange);
    line-height: 1;
  }
  .brand-tagline {
    display: inline-block;
    margin-top: 8px;
    padding: 4px 14px;
    background: var(--charcoal);
    color: var(--paper);
    font-weight: 500;
    font-size: 17px;
    letter-spacing: 2.5px;
  }
  .divider {
    position: absolute;
    left: 520px; top: 60px;
    width: 2px; height: 300px;
    background: linear-gradient(to bottom, rgba(80,80,80,0), #6a6a6a 40%, rgba(80,80,80,0));
  }
  .contact-block {
    position: absolute;
    left: 590px; top: 100px;
  }
  .person-name {
    font-weight: 700;
    font-size: 22px;
    color: var(--orange);
  }
  .person-title {
    font-weight: 500;
    font-size: 15px;
    color: var(--muted);
    margin-top: 2px;
  }
  .contact-list {
    list-style: none;
    margin-top: 54px;
  }
  .contact-list li {
    display: flex;
    align-items: center;
    gap: 12px;
    font-weight: 500;
    font-size: 17px;
    color: var(--ink);
    height: 34px;
  }
  .contact-icon {
    width: 24px; height: 24px;
    flex: none;
  }
  .accent-rule {
    position: absolute;
    left: 0; right: 0;
    top: 448px; height: 6px;
    background: var(--charcoal);
  }
  .accent-band {
    position: absolute;
    left: 0; right: 0;
    top: 454px; height: 20px;
    background: var(--orange);
  }
</style>
</head>
<body>
  <main class="business-card">
    <div class="brand">
      <div class="brand-name">TORVEL</div>
      <div class="brand-tagline">Maintenance Industrielle</div>
    </div>

    <div class="divider"></div>

    <section class="contact-block">
      <h1 class="person-name">Mireille Gauthier</h1>
      <p class="person-title">Owner / Founder</p>
      <ul class="contact-list">
        <li>
          <svg class="contact-icon" viewBox="0 0 24 24" aria-hidden="true">
            <circle cx="12" cy="12" r="12" fill="var(--orange)"/>
            <path d="M6.5 10.5c0-2 2.5-3.5 5.5-3.5s5.5 1.5 5.5 3.5l-2 .5-.5-1.5h-6l-.5 1.5z M8 12h8l1 5H7z" fill="#fff"/>
          </svg>
          (450)-318-5947
        </li>
        <li>
          <svg class="contact-icon" viewBox="0 0 24 24" aria-hidden="true">
            <circle cx="12" cy="12" r="12" fill="var(--orange)"/>
            <rect x="8.5" y="5.5" width="7" height="13" rx="1.2" fill="none" stroke="#fff" stroke-width="1.5"/>
            <circle cx="12" cy="16.3" r="0.9" fill="#fff"/>
          </svg>
          (658) 472-3190
        </li>
        <li>
          <svg class="contact-icon" viewBox="0 0 24 24" aria-hidden="true">
            <circle cx="12" cy="12" r="12" fill="var(--orange)"/>
            <rect x="6" y="8" width="12" height="8.5" fill="#fff"/>
            <path d="M6 8l6 5 6-5" fill="none" stroke="var(--orange)" stroke-width="1.3"/>
          </svg>
          torvel.mnt@boitemel-exemple.com
        </li>
      </ul>
    </section>

    <div class="accent-rule"></div>
    <div class="accent-band"></div>
  </main>
</body>
</html>
```